Fenwick Creek Rodeo Sponsor Brochure/letter

We are wanting a professional looking brochure/letter that can be given to potential sponsors. This can be multiple pages the last page needs to be the Invoice (attached example) the prices on the example can be used.. this is a first nation rodeo and we are looking for sponsorship I can provide more photos if needed

Target Market(s)

This will be local corporate business's so this needs to be very professional looking

Industry/Entity Type

This is an event but we are looking for cooperate sponsorship

Font styles to use
Serif

Colors
0054AA
0677BA
7BADD7
CADEEF
E8F1F8
FFC000
F8CF3A
FAE287
FDF2CF
FEFAEE
F0912C
F2A743
F7CA91
FBE8D2
FDF5EE
EB3D1F
EC4F4E
F09395
F8D3D4
FCEDEE

Requirements
Must have
• The basic information, must have some quotes and photos can be multiple pages
Nice to have
• I would like to see that it is interactive, but gets to the point
Should not have
• no cartoon or must not look cheap

```html
<!DOCTYPE html>
<html lang="en">
<head>
<meta charset="utf-8">
<title>Fenwick Creek Rodeo – Sponsorship Proposal</title>
<link rel="stylesheet" href="https://fonts.googleapis.com/css2?family=Playfair+Display:wght@400;700&family=Lora:wght@400;700&family=Oswald:wght@300;400&family=Bebas+Neue&display=swap">
<style>
:root{
  --ink:#141210;
  --frame:#8a4a24;
  --gold:#f5c430;
  --gold-soft:#e9b94a;
  --white:#f4f1ec;
  --photo-dark:#3a2a1c;
  --photo-mid:#6b5038;
  --photo-light:#9a8468;
}
*{margin:0;padding:0;box-sizing:border-box}
html,body{width:1200px;height:927px;overflow:hidden;background:var(--ink)}
.brochure{position:relative;width:1200px;height:927px;background:radial-gradient(circle at 30% 40%,#1d1a17,var(--ink) 70%);color:var(--white);font-family:"Lora",serif}
.panel{position:absolute;border:2px solid var(--frame);border-radius:3px}
.panel--dates{left:14px;top:15px;width:360px;height:897px}
.panel--about{left:423px;top:1px;width:352px;height:897px}
.panel--cover{left:826px;top:15px;width:351px;height:897px}
.abs{position:absolute}
.dates-title{left:0;width:100%;top:40px;text-align:center;font-family:"Playfair Display",serif;font-weight:700;font-size:36px;color:var(--gold);line-height:1}
.dates-line{left:0;width:100%;top:86px;text-align:center;font-family:"Playfair Display",serif;font-weight:700;font-size:35px;line-height:1;color:var(--white)}
.hat{left:120px;top:120px;width:104px;height:82px;background:linear-gradient(135deg,#e8b835,#b98a1c);border-radius:40% 40% 30% 30%;opacity:.85}
.events-photo{left:28px;top:185px;width:306px;height:452px;background:linear-gradient(160deg,var(--photo-light),var(--photo-mid) 45%,var(--photo-dark));opacity:.55;clip-path:polygon(0 4%,12% 2%,30% 3%,52% 0,75% 3%,100% 1%,100% 96%,80% 98%,60% 97%,40% 100%,20% 97%,0 99%)}
.events-title{left:0;width:100%;top:197px;text-align:center;font-family:"Playfair Display",serif;font-weight:700;font-size:36px;color:var(--gold)}
.badge{width:62px;height:62px}
.badge svg{position:absolute;inset:0}
.badge span{position:absolute;inset:0;display:flex;flex-direction:column;align-items:center;justify-content:center;font-family:"Bebas Neue",sans-serif;font-size:19px;line-height:.85;color:#1a1510}
.event-text{left:88px;width:250px;font-family:"Playfair Display",serif;font-size:15.5px;line-height:23px;color:#ece4d6}
.promo{left:52px;top:477px;width:268px;height:189px;border:4px solid #d9a72a;display:flex;align-items:center;justify-content:center;text-align:center;font-family:"Bebas Neue",sans-serif;font-size:20px;line-height:24.6px;color:var(--gold);letter-spacing:.5px;padding:0 8px}
.intro{left:14px;width:332px;top:694px;text-align:center;font-size:16.5px;line-height:24px;color:var(--white)}
.about-title{left:36px;top:44px;font-family:"Playfair Display",serif;font-weight:700;font-size:36px;color:var(--white)}
.about-body{left:17px;top:107px;width:319px;font-family:"Oswald",sans-serif;font-weight:300;font-size:15.6px;line-height:20.4px;color:var(--gold-soft);text-align:justify}
.cover-title{left:0;width:100%;top:64px;text-align:center;font-family:"Playfair Display",serif;font-weight:700;font-size:52px;line-height:54px;color:var(--white)}
.nation-mark{left:40px;top:262px;width:270px;display:flex;align-items:center;justify-content:center;gap:10px;height:150px;font-family:"Playfair Display",serif;font-weight:700;font-size:21px;line-height:1.2;color:var(--white)}
.nation-mark i{flex:none;width:26px;height:26px;border-radius:50%;background:var(--gold)}
.cover-photo{left:-46px;top:440px;width:396px;height:290px;background:linear-gradient(150deg,#6f6a5e,#6d4a2c 45%,#3f3a2a 80%);opacity:.75;clip-path:polygon(22% 8%,95% 0,100% 40%,92% 70%,70% 92%,30% 100%,8% 80%,0 48%,10% 24%)}
.quote{left:0;width:100%;top:700px;text-align:center;font-family:"Playfair Display",serif;font-weight:700;font-size:19px;line-height:27px;color:var(--white)}
.quote-name{left:0;width:100%;top:759px;text-align:center;font-family:"Playfair Display",serif;font-weight:700;font-size:25px;color:var(--white)}
.site{left:0;width:100%;top:857px;text-align:center;font-size:13px;letter-spacing:6.5px;color:var(--white)}
</style>
</head>
<body>
<main class="brochure">

  <section class="panel panel--dates">
    <h2 class="abs dates-title">Rodeo dates</h2>
    <p class="abs dates-line">July 28, 29, 30 2023</p>
    <div class="abs hat" role="img" aria-label="Gold outline cowboy hat illustration"></div>
    <div class="abs events-photo" role="img" aria-label="Faded photo of cowboys at the rodeo chutes"></div>
    <h3 class="abs events-title">Events</h3>

    <div class="abs badge" style="left:15px;top:235px">
      <svg viewBox="0 0 62 62"><polygon points="31,0 42,8 56,8 58,22 62,31 58,40 56,54 42,54 31,62 20,54 6,54 4,40 0,31 4,22 6,8 20,8" fill="#d6ac3c"/></svg>
      <span>JULY<br>28</span>
    </div>
    <p class="abs event-text" style="top:256px">Gymkhana and family Dance</p>

    <div class="abs badge" style="left:15px;top:320px">
      <svg viewBox="0 0 62 62"><polygon points="31,0 42,8 56,8 58,22 62,31 58,40 56,54 42,54 31,62 20,54 6,54 4,40 0,31 4,22 6,8 20,8" fill="#d6ac3c"/></svg>
      <span>JULY<br>29</span>
    </div>
    <p class="abs event-text" style="top:311px">Junior Rodeo at 11 am, Main Rodeo starts at 2pm with Steak Dinner and Rodeo dance to follow Band is The Silver Sage</p>

    <div class="abs badge" style="left:15px;top:404px">
      <svg viewBox="0 0 62 62"><polygon points="31,0 42,8 56,8 58,22 62,31 58,40 56,54 42,54 31,62 20,54 6,54 4,40 0,31 4,22 6,8 20,8" fill="#d6ac3c"/></svg>
      <span>JULY<br>30</span>
    </div>
    <p class="abs event-text" style="top:413px">July 30 Junior Rodeo at 11 am, Main Rodeo starts at 2pm</p>

    <div class="abs promo">FREE PANCAKE BREAKFAST BOTH SATURDAY AND SUNDAY MORNING CULTURAL EVENTS HAPPENING THROUGHOUT THE DAY.</div>

    <p class="abs intro">Saddle up for the Fenwick Creek Rodeo held at the Fenwick Creek First Nation Rodeo grounds! This is now a 3 day family fun event with the addition of a Friday afternoon Gymkhana! Fenwick Creek Rodeo has been running for over 30 years and we are exciting to bring the excitement back.</p>
  </section>

  <section class="panel panel--about">
    <h2 class="abs about-title">About us</h2>
    <div class="abs about-body">
      <p>One day Rodeos with amazing prizes and buckles each day with the average winning a FCFN Drum! The Fenwick Creek Rodeo is an attraction to many local cowboys and cowgirls from local communities, Fort Alder and across BC, AB and surrounding areas. We offer youth to adult events that are all crowd pleasers.</p>
      <p>Since the beginning this has been an annual event up until Covid-19 when we have had to take a break but we are so excited to build it bigger and better then before!</p>
      <p>We have some big plans for the future of the Fenwick Creek Rodeo including an expansion of the Rodeo grounds, new event buildings, new office/announcer booths as well as the purchase of new grandstands. This will be a big endeavor that we think will benefit both our community as well as the local community. Our rodeo would not have flourished without the support and generosity we have received from your sponsorship over the years. Once again, we are hoping your company will give generously to our yearly event and help continue to make our rodeo a success. All support goes towards any supplies not covered by donation, the purchase of materials to upgrade the rodeo grounds, rodeo stock and event payout. We hope to attract even more roedo events, larger entertainers, and more fans through the gates. Your sponsorship will be highly regarded for what we hope will be generations to come.</p>
      <p>Please see the level of sponsorship attached, fill and return to the Fenwick Creek Rodeo!</p>
      <p>Your sponsorship is greatly appreciated.</p>
      <p>For further information please call or email Marla Tennant 250.555.0142 mtennant@fenwickcreekfn.com</p>
    </div>
  </section>

  <section class="panel panel--cover">
    <h1 class="abs cover-title">Rodeo<br>Sponsorship<br>Proposal</h1>
    <div class="abs nation-mark"><i></i><span>Fenwick Creek<br>First Nation</span></div>
    <div class="abs cover-photo" role="img" aria-label="Photo of a rider on a bucking horse in the arena"></div>
    <p class="abs quote">“Courage is being scared to death<br>and saddling up anyway!”</p>
    <p class="abs quote-name">Hank Dalloway</p>
    <p class="abs site">www.fenwickcreekfn.com</p>
  </section>

</main>
</body>
</html>
```